Moden - Mexicali - Flower Shop

brisapetals is looking for a cool web design that has a airy, clean, mexicali feel to it.

See attached images and links for idea of what we mean with the above.

please no templates.

Target Market(s)

Local flower shop in San Diego, California

Industry/Entity Type

Shop

Requirements
Must have
• see. brisapetals.quartzcart.example - I did the site and logo...I love the logo - hate the site.

Going for this feel: http://www.velmorastudio.example/platebook/archives/tovarinos.php

I also attached another site I liked- I just feel like it may be to busy.

```html
<!DOCTYPE html>
<html lang="en">
<head>
<meta charset="utf-8">
<title>Brisa Petals – Flower Shop</title>
<link href="https://fonts.googleapis.com/css2?family=Bebas+Neue&family=Open+Sans:wght@400;600;700&family=Arvo&family=Libre+Baskerville&family=Questrial&display=swap" rel="stylesheet">
<style>
:root{
  --teal:#3f8a8d;
  --orange:#f5b21d;
  --price:#e0272f;
  --ink:#222;
  --muted:#666;
  --line:#dcdcdc;
  --footer-bar:#3c3c3c;
  --white:#fff;
}
*{box-sizing:border-box;margin:0;padding:0}
html,body{width:763px;height:1200px;overflow:hidden;background:var(--white)}
body{position:relative;font-family:'Open Sans',sans-serif;color:var(--ink)}
.abs{position:absolute}
h1,h2,h3{font-weight:400}

/* header */
.brand{left:76px;top:18px;display:flex;align-items:center;gap:9px;font-family:'Questrial',sans-serif;font-size:21px;letter-spacing:5px;color:var(--teal)}
.brand-dot{width:20px;height:20px;border-radius:50%;background:var(--orange)}
.account-links{top:10px;left:384px;display:flex;gap:20px;font-size:7.5px;color:var(--muted);text-transform:uppercase}
.cart-tab{left:538px;top:0;width:186px;height:28px;background:var(--orange);border-radius:0 0 6px 6px;color:var(--white);font-weight:700;font-size:8px;padding:10px 0 0 9px}
.cart-badge{left:588px;top:2px;width:50px;height:50px;border-radius:50%;background:var(--white);border:3px solid var(--orange);display:flex;align-items:center;justify-content:center}
.cart-total{left:644px;top:6px;color:var(--white);font-weight:700;font-size:13px;white-space:nowrap}
.cart-total sup{font-size:7px}

/* hero */
.hero{left:0;top:60px;width:763px;height:271px;background:linear-gradient(100deg,#b8b58a 0%,#e8d7cf 30%,#d9a1ae 55%,#b5284f 75%,#e9b8c4 100%)}
.nav{left:0;top:60px;width:763px;height:35px;background:rgba(90,90,90,.45)}
.nav ul{list-style:none;display:flex;margin-left:76px;height:35px}
.nav li{font-weight:700;font-size:10px;color:var(--white);padding:0 13px;line-height:35px;text-transform:uppercase}
.nav li.active{background:var(--orange)}
.search{left:508px;top:66px;width:180px;height:22px;background:var(--white);font-size:7px;color:#999;padding:6px 8px}
.search svg{position:absolute;right:6px;top:5px}
.hero-title{left:74px;top:166px;font-family:'Bebas Neue',sans-serif;font-size:64px;color:var(--white);line-height:1}
.hero-sub{left:76px;top:230px;font-family:'Libre Baskerville',serif;font-size:12px;color:#222;line-height:1.35}
.hero-btn{left:76px;top:271px;width:120px;height:36px;background:var(--teal);color:var(--white);font-family:'Bebas Neue',sans-serif;font-size:20px;display:flex;align-items:center;justify-content:center}
.hero-arrow{top:198px;width:26px;height:28px;background:var(--white);display:flex;align-items:center;justify-content:center}
.dots{left:644px;top:307px;display:flex;gap:4px}
.dots span{width:11px;height:11px;border-radius:50%;background:var(--white)}
.dots span:first-child{background:#111}

/* sections */
.section-title{left:76px;font-family:'Arvo',serif;font-size:13.5px;color:#222}
.rule{left:76px;width:610px;height:1px;background:var(--line)}
.rule i{position:absolute;left:0;top:-1px;width:113px;height:3px;background:var(--teal)}
.pager{left:659px;display:flex;gap:2px}
.card{width:139px;border:1px solid var(--line);text-align:center}
.card.accent{border-color:#f6d7bf}
.photo{position:absolute;left:7px;top:6px;width:124px;height:117px}
.card-text{position:absolute;left:0;width:100%;font-size:8.3px;line-height:1.4;color:#222}
.price{position:absolute;left:0;width:100%;font-size:13px;color:var(--price)}
.price s{color:#9a9a9a;margin-left:4px}
.btn{position:absolute;left:29px;width:80px;height:26px;color:var(--white);font-family:'Bebas Neue',sans-serif;font-size:15px;display:flex;align-items:center;justify-content:center;background:var(--teal)}
.btn.warm{background:var(--orange)}
.card-name{position:absolute;left:0;width:100%;font-size:9px;font-weight:600}
.count{position:absolute;left:0;width:100%;font-size:8.5px;color:var(--price)}

/* newsletter */
.newsletter{left:0;top:887px;width:763px;height:173px;background:linear-gradient(90deg,#3a3436 0%,#4a3a40 60%,#5a3b48 100%)}
.nl-title{left:0;width:763px;top:911px;text-align:center;font-family:'Bebas Neue',sans-serif;font-size:28px;color:var(--orange)}
.nl-text{left:0;width:763px;top:945px;text-align:center;font-size:15.5px;color:var(--white)}
.nl-input{left:195px;top:976px;width:305px;height:26px;background:var(--white)}
.nl-submit{left:504px;top:976px;width:83px;height:26px;background:var(--orange);color:var(--white);font-family:'Bebas Neue',sans-serif;font-size:15px;display:flex;align-items:center;justify-content:center}

/* footer */
.f-head{top:1073px;font-size:8px;font-weight:700;text-transform:uppercase;color:#222}
.f-list{top:1092px;font-size:8.2px;line-height:15px;color:#333;list-style:none}
.f-divider{top:1070px;width:1px;height:95px;background:var(--line)}
.map{left:165px;top:1093px;width:132px;height:66px;background:linear-gradient(135deg,#d9d6cc,#c9cfc4)}
.f-address{left:305px;top:1089px;font-size:8.2px;line-height:15px;color:#333}
.f-address u{color:#a07000;font-style:italic}
.social{left:447px;top:1089px;font-size:8.2px;color:#333;list-style:none}
.social li{display:flex;align-items:center;gap:6px;height:20px}
.social i{width:14px;height:14px;background:#555;display:block}
.about{left:558px;top:1089px;width:130px;font-size:8.2px;line-height:15px;color:#333}
.footer-bar{left:0;top:1172px;width:763px;height:28px;background:var(--footer-bar);color:var(--white);font-size:8px;padding:9px 0 0 76px}
</style>
</head>
<body>

<header>
  <div class="abs brand"><span class="brand-dot"></span>BRISA PETALS</div>
  <div class="abs account-links"><span>My Account</span><span>Log In</span><span>Register</span></div>
  <div class="abs cart-tab">MY CART</div>
  <div class="abs cart-badge">
    <svg width="26" height="24" viewBox="0 0 26 24"><path d="M3 4h4l3 11h11l3-8H9" fill="none" stroke="#e0272f" stroke-width="2"/><circle cx="11" cy="19" r="2" fill="#e0272f"/><circle cx="20" cy="19" r="2" fill="#e0272f"/><text x="12" y="11" font-size="7" font-family="Open Sans" font-weight="700" fill="#222">20</text></svg>
  </div>
  <div class="abs cart-total">$352<sup>.00</sup></div>
</header>

<section>
  <div class="abs hero" role="img" aria-label="Close-up photo of pink and white dianthus flowers"></div>
  <nav class="abs nav"><ul><li class="active">Home</li><li>Shop</li><li>Curated</li><li>About Us</li></ul></nav>
  <div class="abs search">Search Entire Store here...
    <svg width="10" height="10" viewBox="0 0 10 10"><circle cx="4" cy="4" r="3" fill="none" stroke="#666" stroke-width="1.3"/><path d="M6.3 6.3 9 9" stroke="#666" stroke-width="1.3"/></svg>
  </div>
  <h1 class="abs hero-title">NEW ARRIVALS</h1>
  <p class="abs hero-sub">Excepteur sint occaecat cupidatat non proident,<br>sunt in culpa qui.</p>
  <div class="abs hero-btn">SHOP NOW</div>
  <div class="abs hero-arrow" style="left:0"><svg width="8" height="10"><path d="M6 1 2 5l4 4" fill="none" stroke="#e0272f" stroke-width="1.5"/></svg></div>
  <div class="abs hero-arrow" style="left:737px"><svg width="8" height="10"><path d="M2 1l4 4-4 4" fill="none" stroke="#e0272f" stroke-width="1.5"/></svg></div>
  <div class="abs dots"><span></span><span></span><span></span></div>
</section>

<section>
  <h2 class="abs section-title" style="top:348px">Fresh This Week</h2>
  <div class="abs rule" style="top:369px"><i></i></div>
  <div class="abs pager" style="top:360px">
    <svg width="12" height="16"><path d="M9 2 3 8l6 6" fill="none" stroke="#f5b21d" stroke-width="1.5"/></svg>
    <svg width="12" height="16"><path d="M3 2l6 6-6 6" fill="none" stroke="#999" stroke-width="1.5"/></svg>
  </div>

  <div class="abs card accent" style="left:76px;top:382px;height:210px">
    <div class="photo" role="img" aria-label="Orange and yellow lilies in a paper wrap" style="background:linear-gradient(135deg,#e8b13a,#d3652a,#7d8b3a)"></div>
    <p class="card-text" style="top:128px">Lorem Ipsum is simply<br>dummy text of the printing</p>
    <p class="price" style="top:153px">$50.00<s>$75.00</s></p>
    <div class="btn warm" style="top:175px">BUY NOW</div>
  </div>
  <div class="abs card" style="left:233px;top:382px;height:210px">
    <div class="photo" role="img" aria-label="Bunches of deep red roses on wood" style="background:linear-gradient(135deg,#5e0f1a,#8d1a26,#4a1515)"></div>
    <p class="card-text" style="top:128px">Lorem Ipsum is simply<br>dummy text of the printing</p>
    <p class="price" style="top:153px">$100.00</p>
    <div class="btn" style="top:175px">BUY NOW</div>
  </div>
  <div class="abs card" style="left:391px;top:382px;height:210px">
    <div class="photo" role="img" aria-label="Pink and white stargazer lilies with green leaves" style="background:linear-gradient(135deg,#e9d5db,#c9829c,#3f6b35)"></div>
    <p class="card-text" style="top:128px">Lorem Ipsum is simply<br>dummy text of the printing</p>
    <p class="price" style="top:153px">$40.00</p>
    <div class="btn" style="top:175px">BUY NOW</div>
  </div>
  <div class="abs card" style="left:548px;top:382px;height:210px">
    <div class="photo" role="img" aria-label="Pink gerbera daisies wrapped in kraft paper" style="background:linear-gradient(135deg,#8a8a86,#e0568a,#b58a5e)"></div>
    <p class="card-text" style="top:128px">Lorem Ipsum is simply<br>dummy text of the printing</p>
    <p class="price" style="top:153px">$50.00</p>
    <div class="btn warm" style="top:175px">BUY NOW</div>
  </div>
</section>

<section>
  <h2 class="abs section-title" style="top:614px">Curated Collection</h2>
  <div class="abs rule" style="top:634px"><i></i></div>
  <div class="abs pager" style="top:625px">
    <svg width="12" height="16"><path d="M9 2 3 8l6 6" fill="none" stroke="#f5b21d" stroke-width="1.5"/></svg>
    <svg width="12" height="16"><path d="M3 2l6 6-6 6" fill="none" stroke="#999" stroke-width="1.5"/></svg>
  </div>

  <div class="abs card accent" style="left:76px;top:647px;height:210px">
    <div class="photo" role="img" aria-label="White calla lilies on weathered wood" style="background:linear-gradient(135deg,#6d6a63,#e9ece4,#5b7f3a)"></div>
    <p class="card-name" style="top:129px">Dude</p>
    <p class="count" style="top:149px">2 Products</p>
    <div class="btn warm" style="top:175px">VIEW MORE</div>
  </div>
  <div class="abs card" style="left:233px;top:647px;height:210px">
    <div class="photo" role="img" aria-label="Bunches of deep red roses on wood" style="background:linear-gradient(135deg,#5e0f1a,#8d1a26,#4a1515)"></div>
    <p class="card-name" style="top:129px">Love</p>
    <p class="count" style="top:149px">1 Products</p>
    <div class="btn" style="top:175px">VIEW MORE</div>
  </div>
  <div class="abs card" style="left:391px;top:647px;height:210px">
    <div class="photo" role="img" aria-label="Pink and white stargazer lilies with green leaves" style="background:linear-gradient(135deg,#e9d5db,#c9829c,#3f6b35)"></div>
    <p class="card-name" style="top:129px">Any Occasion</p>
    <p class="count" style="top:149px">2 Products</p>
    <div class="btn" style="top:175px">VIEW MORE</div>
  </div>
  <div class="abs card" style="left:548px;top:647px;height:210px">
    <div class="photo" role="img" aria-label="Pink gerbera daisies wrapped in kraft paper" style="background:linear-gradient(135deg,#8a8a86,#e0568a,#b58a5e)"></div>
    <p class="card-name" style="top:129px">Birthday</p>
    <p class="count" style="top:149px">2 Products</p>
    <div class="btn" style="top:175px">VIEW MORE</div>
  </div>
</section>

<section>
  <div class="abs newsletter" role="img" aria-label="Dark, soft-focus photo of pink flower petals"></div>
  <h2 class="abs nl-title">NEWSLETTER</h2>
  <p class="abs nl-text">We promise to only send you good things like discounts!</p>
  <div class="abs nl-input"></div>
  <div class="abs nl-submit">SUBMIT</div>
</section>

<footer>
  <h3 class="abs f-head" style="left:76px">Quick Links</h3>
  <ul class="abs f-list" style="left:76px"><li>Home</li><li>Shop</li><li>Curated</li><li>About Us</li></ul>
  <div class="abs f-divider" style="left:155px"></div>

  <h3 class="abs f-head" style="left:165px">Reach Brisa</h3>
  <div class="abs map" role="img" aria-label="Street map showing the shop location"></div>
  <svg class="abs" style="left:222px;top:1110px" width="12" height="16" viewBox="0 0 12 16"><path d="M6 15C2 9 1 7 1 5a5 5 0 0 1 10 0c0 2-1 4-5 10z" fill="#e0272f"/><circle cx="6" cy="5" r="2" fill="#fff"/></svg>
  <p class="abs f-address">2210 Marisol Avenue<br>San Diego, CA 92104<br>Email: info@brisapetals.example<br>Phone: 619-555-0184<br><u>View location</u></p>
  <div class="abs f-divider" style="left:430px"></div>

  <h3 class="abs f-head" style="left:447px">Get Social</h3>
  <ul class="abs social"><li><i></i>Chirpline</li><li><i></i>Facetome</li><li><i></i>plusring</li></ul>
  <div class="abs f-divider" style="left:540px"></div>

  <h3 class="abs f-head" style="left:558px">About Brisa</h3>
  <p class="abs about">Based in Hillcrest, San Diego - We offer farm fresh, curated, cool, and same day delivery flower bouquets.</p>

  <div class="abs footer-bar">Copyright © 2014 brisapetals of San Diego.</div>
</footer>

</body>
</html>
```